KEV.PRO- Darren Holcombe Fitness- needs a clever business card using the logo, name, info, contact

I need a business card designed for my Online Personal Training company called KEV.PRO, abbreviation for Darren Holcombe Fitness. My company focuses on coaching in personal health and personal growth to unleash your greatest potential. I would like to see designs that use my color scheme of a redish-orange (C:0,M:84,Y:100,K:0), grey, white, black, and my company font is OSWALD. The final design should communicate some aspects of design, health, motivation, growth, in some way. The logo is very important to the company and can be displayed in any of the colors previously mentioned. Must include the company name, my website: www.kev-pro.example , my email: dan@kev-pro.example

Target Market(s)

Personal health, fitness, general public, those who lack knowledge, awareness, and confidence in personal health

Industry/Entity Type

Personal Trainer

Font styles to use
Other font styles liked:
• OSWALD. (Bold, Regular, Light)

Colors
f37122
ffffff
9d9d9d
000000

Requirements
Must have
• Must include the logo, company name, my website: www.kev-pro.example , my email: dan@kev-pro.example
Nice to have
• Variations of the colors scheme of a redish-orange (C:0,M:84,Y:100,K:0), grey, white, black. Logo, card, or text can be in any of these colors.
• Possible quote like "Take control of your personal health to unleash your greatest potential" or "Unleashing your greatness first begins with fitness of the body and mind"

```html
<!DOCTYPE html>
<html lang="en">
<head>
<meta charset="utf-8">
<title>KEV.PRO – Business Card</title>
<link href="https://fonts.googleapis.com/css2?family=Oswald:wght@300;400;700&display=swap" rel="stylesheet">
<style>
  :root {
    --brand-orange: #f37122;
    --brand-red: #c8380f;
    --brand-orange-soft: #e87a55;
    --brand-peach: #f1c9b4;
    --ink: #111111;
    --paper: #f4f4f2;
    --grey: #9d9d9d;
    --backdrop: #d5dada;
  }
  * { margin: 0; padding: 0; box-sizing: border-box; }
  html, body {
    width: 1200px;
    height: 1200px;
    overflow: hidden;
    background: var(--backdrop);
    font-family: "Oswald", sans-serif;
  }
  .sheet {
    width: 1200px;
    height: 1200px;
    display: flex;
    flex-direction: column;
    align-items: center;
    justify-content: center;
    gap: 50px;
  }
  .card {
    width: 860px;
    height: 491px;
    display: block;
    box-shadow: 0 14px 30px rgba(0,0,0,0.18);
  }
  .card-text { font-family: "Oswald", sans-serif; }
  .stack-name { font-weight: 400; font-size: 30px; letter-spacing: 9px; fill: var(--ink); }
  .contact-line { font-weight: 400; font-size: 26px; letter-spacing: 1px; fill: #ffffff; }
  .brand-mark { font-weight: 700; fill: var(--brand-red); }
  .brand-faint { font-weight: 700; fill: var(--brand-peach); }
  .brand-title { font-weight: 700; fill: var(--ink); }
</style>
</head>
<body>
<main class="sheet">

  <svg class="card card-front" viewBox="0 0 860 491" xmlns="http://www.w3.org/2000/svg" aria-label="KEV.PRO business card, contact side">
    <rect width="860" height="491" fill="var(--paper)"/>

    <g class="brand-watermark">
      <circle cx="150" cy="120" r="95" fill="none" stroke="var(--brand-peach)" stroke-width="10"/>
      <text class="card-text brand-faint" x="150" y="136" font-size="44" text-anchor="middle">KEV.PRO</text>
    </g>

    <g class="stack-name-block">
      <text class="card-text stack-name" x="278" y="72">DARREN</text>
      <text class="card-text stack-name" x="278" y="114">HOLCOMBE</text>
      <text class="card-text stack-name" x="278" y="156">FITNESS</text>
    </g>

    <path class="swoosh" d="M0,232 C110,262 220,268 310,246 C220,284 100,282 0,262 Z" fill="var(--brand-red)"/>

    <path class="wave-dark" d="M0,300 C150,270 260,300 330,230 C400,160 520,105 860,95 L860,491 L0,491 Z" fill="var(--ink)"/>

    <path class="band-soft" d="M0,372 C170,392 330,448 430,491 L0,491 Z" fill="var(--brand-orange-soft)"/>
    <path class="band-strong" d="M0,400 C150,416 290,460 360,491 L0,491 Z" fill="var(--brand-red)"/>

    <g class="contact-list">
      <g transform="translate(362,238)" fill="none" stroke="#ffffff" stroke-width="2">
        <rect x="0" y="0" width="30" height="21"/>
        <path d="M0,0 L15,12 L30,0"/>
      </g>
      <text class="card-text contact-line" x="418" y="258">dan@kev-pro.example</text>

      <path transform="translate(362,292)" d="M6,0 L12,0 L14,8 L10,11 C12,17 15,20 20,22 L23,18 L31,20 L31,26 C31,28 29,30 27,30 C12,29 1,18 0,4 C0,2 2,0 6,0 Z" fill="#ffffff"/>
      <text class="card-text contact-line" x="418" y="318">+1 - 555 - 010 - 0199</text>

      <g transform="translate(377,369)" fill="none" stroke="#ffffff" stroke-width="2">
        <circle cx="0" cy="0" r="14"/>
        <ellipse cx="0" cy="0" rx="6" ry="14"/>
        <path d="M-14,0 H14 M-12,-7 H12 M-12,7 H12"/>
      </g>
      <text class="card-text contact-line" x="418" y="378">www.kev-pro.example</text>
    </g>

    <g class="brand-small">
      <circle cx="772" cy="228" r="56" fill="none" stroke="var(--brand-red)" stroke-width="6"/>
      <text class="card-text brand-mark" x="772" y="237" font-size="25" text-anchor="middle">KEV.PRO</text>
    </g>
  </svg>

  <svg class="card card-back" viewBox="0 0 860 491" xmlns="http://www.w3.org/2000/svg" aria-label="KEV.PRO business card, brand side">
    <rect width="860" height="491" fill="var(--brand-red)"/>
    <ellipse cx="430" cy="245" rx="415" ry="300" fill="var(--brand-orange-soft)"/>
    <ellipse cx="430" cy="245" rx="400" ry="290" fill="var(--ink)"/>
    <ellipse cx="420" cy="245" rx="390" ry="290" fill="var(--paper)"/>

    <g class="brand-center">
      <circle cx="430" cy="175" r="88" fill="none" stroke="var(--brand-red)" stroke-width="8"/>
      <text class="card-text brand-title" x="430" y="340" font-size="58" text-anchor="middle">KEV.PRO</text>
    </g>
  </svg>

</main>
</body>
</html>
```